Letterhead

We are looking for a basic letterhead. It should include our logo, website - northpeakkitchenware.com, phone 907.418.3952, toll free 855.392.6180, and fax 907.418.5263, along with our address 4837 Birchwood Lane, Anchorage, AK 99517. I want something that will look good printed in color or black and white.

```html
<!DOCTYPE html>
<html lang="en">
<head>
<meta charset="utf-8">
<title>North Peak Kitchenware – Letterhead</title>
<link rel="stylesheet" href="https://fonts.googleapis.com/css2?family=Montserrat:wght@500;600;700;800&display=swap">
<style>
  :root {
    --backdrop: #d9b56e;
    --paper: #ffffff;
    --brand-blue: #1f4384;
    --brand-red: #c13748;
    --ink-black: #1c1c1c;
  }
  * { margin: 0; padding: 0; box-sizing: border-box; }
  html, body { width: 1200px; height: 900px; overflow: hidden; }
  body {
    background: var(--backdrop);
    font-family: "Montserrat", Arial, sans-serif;
    position: relative;
  }
  .sheet {
    --text: var(--brand-blue);
    --accent: var(--brand-red);
    position: absolute;
    top: 124px;
    width: 529px;
    height: 676px;
    background: var(--paper);
    box-shadow: 0 1px 4px rgba(0,0,0,0.18);
    overflow: hidden;
  }
  .sheet--color { left: 38px; }
  .sheet--mono {
    left: 626px;
    --text: var(--ink-black);
    --accent: var(--ink-black);
  }
  .brand-name {
    position: absolute;
    left: 14px;
    top: 46px;
    color: var(--text);
    font-weight: 800;
    line-height: 1;
    text-transform: uppercase;
  }
  .brand-name__main { display: block; font-size: 27px; letter-spacing: -0.5px; }
  .brand-name__sub { display: block; font-size: 10.5px; letter-spacing: 1.5px; margin-top: 5px; }

  .contact {
    position: absolute;
    right: 11px;
    top: 9px;
    list-style: none;
    color: var(--text);
    font-size: 12.5px;
    font-weight: 500;
    line-height: 15px;
  }
  .contact__item {
    display: flex;
    align-items: center;
    justify-content: flex-end;
    gap: 6px;
    margin-bottom: 4px;
  }
  .contact__item--address { align-items: flex-start; margin-bottom: 2px; }
  .contact__icon { width: 20px; height: 20px; fill: var(--accent); flex: none; }

  .website {
    position: absolute;
    right: 13px;
    bottom: 43px;
    color: var(--text);
    font-size: 13.5px;
    font-weight: 500;
  }
  .website__icon {
    display: block;
    width: 28px;
    height: 28px;
    margin-bottom: 4px;
    fill: none;
    stroke: var(--accent);
    stroke-width: 1.8;
  }
  .footer-band {
    position: absolute;
    left: 0;
    bottom: 0;
    width: 100%;
    height: 60px;
    background: linear-gradient(to bottom, rgba(255,255,255,0) 0%, var(--accent) 100%);
    opacity: 0.85;
  }
</style>
</head>
<body>

<svg width="0" height="0" style="position:absolute" aria-hidden="true">
  <symbol id="icon-home" viewBox="0 0 24 24"><path d="M12 2 1 12h3v10h6v-6h4v6h6V12h3z"/></symbol>
  <symbol id="icon-phone" viewBox="0 0 24 24"><path d="M6.6 2.5 9.8 6c.5.6.5 1.4 0 2l-1.6 1.7c1.3 2.7 3.4 4.8 6.1 6.1L16 14.2c.6-.5 1.4-.5 2 0l3.5 3.2c.6.6.6 1.5 0 2.1l-1.8 1.8c-1 1-2.5 1.3-3.8.8C9.7 19.7 4.3 14.3 1.9 8.1c-.5-1.3-.2-2.8.8-3.8l1.8-1.8c.6-.6 1.5-.6 2.1 0z"/></symbol>
  <symbol id="icon-mobile" viewBox="0 0 24 24"><path d="M7 1h10a2 2 0 0 1 2 2v18a2 2 0 0 1-2 2H7a2 2 0 0 1-2-2V3a2 2 0 0 1 2-2zm1 3v10h8V4zm0 12v2h2v-2zm3 0v2h2v-2zm3 0v2h2v-2zm-6 3v2h2v-2zm3 0v2h2v-2zm3 0v2h2v-2z"/></symbol>
  <symbol id="icon-fax" viewBox="0 0 24 24"><path d="M6 1h12v6H6zM3 8h18a2 2 0 0 1 2 2v9h-4v4H5v-4H1v-9a2 2 0 0 1 2-2zm4 7v6h10v-6zm1 1h8v1H8zm0 2h8v1H8z"/></symbol>
  <symbol id="icon-globe" viewBox="0 0 28 28"><circle cx="14" cy="14" r="12"/><ellipse cx="14" cy="14" rx="5.5" ry="12"/><path d="M2 14h24M4 8h20M4 20h20M14 2v24"/></symbol>
</svg>

<article class="sheet sheet--color" aria-label="Letterhead, colour version">
  <h1 class="brand-name"><span class="brand-name__main">North Peak</span><span class="brand-name__sub">Kitchenware</span></h1>
  <ul class="contact">
    <li class="contact__item contact__item--address"><svg class="contact__icon"><use href="#icon-home"/></svg><span>4837 Birchwood Lane,<br>Anchorage, AK 99517</span></li>
    <li class="contact__item"><svg class="contact__icon"><use href="#icon-phone"/></svg><span>855.392.6180</span></li>
    <li class="contact__item"><svg class="contact__icon"><use href="#icon-mobile"/></svg><span>907.418.3952</span></li>
    <li class="contact__item"><svg class="contact__icon"><use href="#icon-fax"/></svg><span>907.418.5263</span></li>
  </ul>
  <div class="footer-band" role="img" aria-label="Decorative footer artwork in brand red"></div>
  <div class="website"><svg class="website__icon"><use href="#icon-globe"/></svg>northpeakkitchenware.com</div>
</article>

<article class="sheet sheet--mono" aria-label="Letterhead, black and white version">
  <h1 class="brand-name"><span class="brand-name__main">North Peak</span><span class="brand-name__sub">Kitchenware</span></h1>
  <ul class="contact">
    <li class="contact__item contact__item--address"><svg class="contact__icon"><use href="#icon-home"/></svg><span>4837 Birchwood Lane,<br>Anchorage, AK 99517</span></li>
    <li class="contact__item"><svg class="contact__icon"><use href="#icon-phone"/></svg><span>855.392.6180</span></li>
    <li class="contact__item"><svg class="contact__icon"><use href="#icon-mobile"/></svg><span>907.418.3952</span></li>
    <li class="contact__item"><svg class="contact__icon"><use href="#icon-fax"/></svg><span>907.418.5263</span></li>
  </ul>
  <div class="footer-band" role="img" aria-label="Decorative footer artwork in black"></div>
  <div class="website"><svg class="website__icon"><use href="#icon-globe"/></svg>northpeakkitchenware.com</div>
</article>

</body>
</html>
```